Business Recognition Design

We need a design for a recognition to be given to business leaders in our community.
The recognition shall be made on a brass plaque on wood panel background (picture attached, please use it as a background), and all drawing must be in vectors and only one color (black).
It should also have a logo on the top and signature on the right bottom.
The text is enclosed in DOC file.

Reason: just to be able to find the best solution

Reason: None of the suggestion is good enough. Logo in general is too big in comparison with the rest of the plate.

Industry/Entity Type

Business

Requirements
Must have
• - standard Windows font (or possibility to install the same font on Windows), as the name on the recognition shall be printed in the same font
Nice to have
• - some graphic element (in curves) representing achievements in business
- should look great :)

```html
<!DOCTYPE html>
<html lang="de">
<head>
<meta charset="utf-8">
<title>Auszeichnung – Kronfeld</title>
<link rel="stylesheet" href="https://fonts.googleapis.com/css2?family=Tinos:wght@400;700&display=swap">
<style>
  :root {
    --backdrop: #3b3b3b;
    --wood-dark: #4a2c17;
    --wood-mid: #6b4326;
    --wood-light: #835633;
    --brass-light: #f4d867;
    --brass-mid: #e2b93a;
    --brass-dark: #c3951f;
    --ink: #1e1a10;
    --screw-light: #f7e08a;
    --screw-dark: #8a6510;
  }
  * { margin: 0; padding: 0; box-sizing: border-box; }
  html, body { width: 1200px; height: 832px; overflow: hidden; }
  body {
    position: relative;
    background: var(--backdrop);
    font-family: "Tinos", "Times New Roman", serif;
    color: var(--ink);
  }
  .wood-panel {
    position: absolute;
    left: 168px; top: 33px;
    width: 864px; height: 665px;
    background: linear-gradient(135deg, var(--wood-light), var(--wood-mid) 45%, var(--wood-dark));
    border: 6px solid var(--wood-dark);
    border-top-color: var(--wood-light);
    border-left-color: var(--wood-light);
  }
  .brass-plate {
    position: absolute;
    left: 192px; top: 57px;
    width: 816px; height: 618px;
    background: linear-gradient(160deg, var(--brass-light), var(--brass-mid) 50%, var(--brass-dark));
    border: 2px solid var(--brass-dark);
  }
  .screw {
    position: absolute;
    width: 18px; height: 18px;
    margin: -9px 0 0 -9px;
    border-radius: 50%;
    background: radial-gradient(circle at 35% 35%, var(--screw-light), var(--brass-mid) 50%, var(--screw-dark));
  }
  .screw.tl { left: 232px; top: 93px; }
  .screw.tr { left: 976px; top: 93px; }
  .screw.bl { left: 232px; top: 636px; }
  .screw.br { left: 976px; top: 636px; }

  .line { position: absolute; left: 267px; line-height: 1; white-space: nowrap; }

  .brand {
    top: 163px;
    display: flex; align-items: center; gap: 10px;
    font-weight: 700; font-size: 34px;
  }
  .brand-mark { width: 16px; height: 16px; background: var(--ink); border-radius: 50%; }

  .award-title { top: 214px; font-size: 43px; font-weight: 400; letter-spacing: 0.5px; }
  .award-subtitle { font-size: 31px; font-weight: 700; }
  .award-subtitle.first { top: 263px; }
  .award-subtitle.second { top: 302px; }
  .award-for { top: 342px; font-size: 20px; }
  .recipient { top: 371px; font-size: 28px; font-weight: 700; }
  .citation { font-size: 20px; }
  .citation.l1 { top: 402px; }
  .citation.l2 { top: 440px; }
  .citation.l3 { top: 468px; }
  .citation.l4 { top: 500px; }
  .citation strong { font-size: 22px; }
  .citation .name-small { font-size: 13px; font-weight: 700; }
  .signature-line { top: 600px; font-size: 20px; }

  .achievement-figure {
    position: absolute;
    left: 722px; top: 168px;
    width: 238px; height: 470px;
    background: linear-gradient(180deg, rgba(20,16,8,0.78), rgba(20,16,8,0.92));
    border-radius: 6px;
  }
</style>
</head>
<body>
  <div class="wood-panel"></div>
  <div class="brass-plate"></div>
  <span class="screw tl"></span>
  <span class="screw tr"></span>
  <span class="screw bl"></span>
  <span class="screw br"></span>

  <div class="line brand">
    <span class="brand-mark"></span>
    <span class="brand-name">Kronfeld</span>
  </div>

  <h1 class="line award-title">AUSZEICHNUNG</h1>
  <p class="line award-subtitle first">als herausragendster</p>
  <p class="line award-subtitle second">Unternehmer Deutschlands 2013</p>
  <p class="line award-for">für</p>
  <p class="line recipient">Herrn Dipl.-Kfm. Paul Kramer</p>
  <p class="line citation l1">Unter der Leitung von <strong>Herr Dipl.-Kfm.</strong> <span class="name-small">Paul Kramer</span></p>
  <p class="line citation l2">hat sich die FIRMA GmbH im Jahr 2013 unter</p>
  <p class="line citation l3">den ersten 5% der größten deutschen</p>
  <p class="line citation l4">Wirtschaftsunternehmen platziert.</p>

  <p class="line signature-line">Feldheim, 20. Juni 2013 Lena Brandt</p>

  <div class="achievement-figure" role="img" aria-label="Black silhouette of a businessman raising a trophy while standing on a target"></div>
</body>
</html>
```